Flyer Design Project for lawn care business

I need a flyer designed for my lawn care business, "Ashby's Groundcare Services".  It is a family owned small landscaping company. I was thinking something that I can print  2- 3 per page.
I have  2 different logos I can upload to give an idea.  I have seen some I like that are colorfull with neat graphics but I also like some that are simple and elegant.  I would like something that catches your eye and looks professionaly done.

Target Market(s)
Homeowners in Durham, North Carolina with homes usually valued $200,000 or more.
Industry/Entity Type
Landscaping
Requirements
Must have
- I would like the address of my website listed on it, www.ashbygroundcareservices.com
I would like for it to say somewhere, 50% off first service with seasonal service.
Not sure if I want to list some of the services that I offer or just say full service lawn care.
Nice to have
- I have a logo with a bull pushing a lawn mower.  I live in Durham, NC also known as the Bull City.  I am not in love with the logo so feel free to change it or not use it at all.

```html
<!DOCTYPE html>
<html lang="en">
<head>
<meta charset="utf-8">
<title>Ashby's Groundcare Services – Flyer</title>
<link rel="stylesheet" href="https://fonts.googleapis.com/css2?family=Fira+Sans:wght@500;600&family=Poppins:wght@500;600&display=swap">
<style>
  :root {
    --page: #ffffff;
    --grass-dark: #3f8f14;
    --grass-light: #7fd43a;
    --soil-dark: #3a2218;
    --soil-mid: #5a3a2a;
    --brand-green: #7cf200;
    --ink-white: #ffffff;
  }
  html, body {
    margin: 0;
    padding: 0;
    width: 1200px;
    height: 932px;
    overflow: hidden;
    background: var(--page);
  }
  .flyer {
    position: absolute;
    left: 50px;
    top: 79px;
    width: 1100px;
    height: 774px;
    overflow: hidden;
    color: var(--ink-white);
    text-align: center;
  }
  .flyer__backdrop {
    position: absolute;
    inset: 0;
    background:
      linear-gradient(90deg,
        var(--grass-light) 0%, var(--grass-dark) 8%, var(--grass-light) 14%, var(--grass-dark) 16.5%,
        var(--soil-dark) 18%, var(--soil-mid) 35%, var(--soil-dark) 50%, var(--soil-mid) 68%, var(--soil-dark) 84.5%,
        var(--grass-dark) 86%, var(--grass-light) 90%, var(--grass-dark) 95%, var(--grass-light) 100%);
  }
  .flyer__brand {
    position: absolute;
    left: 0;
    right: 0;
    top: 60px;
    margin: 0;
    font-family: "Poppins", sans-serif;
    font-weight: 600;
    font-size: 140px;
    line-height: 1;
    letter-spacing: 2px;
    color: var(--brand-green);
    -webkit-text-stroke: 6px var(--ink-white);
    paint-order: stroke fill;
  }
  .flyer__tagline {
    position: absolute;
    left: 0;
    right: 0;
    top: 230px;
    margin: 0;
    font-family: "Fira Sans", sans-serif;
    font-weight: 600;
    font-size: 58px;
    line-height: 1;
    letter-spacing: 1px;
  }
  .offer {
    position: absolute;
    left: 250px;
    top: 330px;
    width: 600px;
    transform: rotate(-9deg);
    font-family: "Poppins", sans-serif;
    font-weight: 600;
  }
  .offer__headline {
    display: block;
    font-size: 108px;
    line-height: 1;
    letter-spacing: -2px;
  }
  .offer__terms {
    display: block;
    font-size: 66px;
    line-height: 62px;
  }
  .flyer__web {
    position: absolute;
    left: 0;
    right: 0;
    top: 704px;
    margin: 0;
    font-family: "Fira Sans", sans-serif;
    font-weight: 500;
    font-size: 37px;
    line-height: 1;
  }
</style>
</head>
<body>
  <main class="flyer">
    <div class="flyer__backdrop" role="img" aria-label="Photo of rich brown soil framed by strips of green grass on the left and right edges"></div>
    <h1 class="flyer__brand">ASHBYS</h1>
    <p class="flyer__tagline">FULL SERVICE LAWN CARE</p>
    <p class="offer">
      <span class="offer__headline">50%OFF</span>
      <span class="offer__terms">first service<br>with seasonal<br>service</span>
    </p>
    <p class="flyer__web">www.ashbygroundcareservices.com</p>
  </main>
</body>
</html>
```